New Brochure Design for multiple brochures

We are looking for a designer to create a new template for our vitaRUN family of modular and mobile biopharmaceutical facilities. We will be looking to put together a set of new brochures based on this design, likely using the original designer to complete the final layouts. The attached brochure is true to our current aesthetic and contains our basic corporate color scheme. However, we are open to changes to the colors and the overall look so long as they work with our logo. (FYI: Our president favors clean designs with abundant white space.) Overall, we are hoping to achieve a design that projects the high-tech nature of our company and equipment. This equipment is designed for and sold to biotech and pharmaceutical companies and the brochures should cater to that audience in their visual style.

Target Market(s)

Pharmaceutical Industry

Industry/Entity Type

Biotechnology

Font styles to use
Sans Serif

Requirements
Must have
• A layout design that provides a fresh look on the current brochures attached to this brief. The desired layout would have clean lines with a technology company feel. White space and a design that has a layout with sufficient spacing is important.
Nice to have
• Really like the idea of having a theme that emphasizes a product life cycle and conveys life science technology (gene therapy, cancer drug development) focus.
Should not have
• Cluttered objects and text. Must use the current logo format.

```html
<!DOCTYPE html>
<html lang="en">
<head>
<meta charset="utf-8">
<title>vitaRUN Brochure Spread</title>
<link href="https://fonts.googleapis.com/css2?family=Montserrat:wght@400;700;800;900&display=swap" rel="stylesheet">
<style>
  :root{
    --backdrop:#9a99a3;
    --paper:#ffffff;
    --navy:#1c2f8e;
    --ink:#4a4d57;
    --muted:#b4b6bd;
    --photo-blue:#7f95bd;
    --photo-deep:#4e648e;
    --photo-night:#1b2130;
    --lab-light:#e4e2de;
    --lab-mid:#b9b4aa;
  }
  html,body{margin:0;padding:0;}
  body{
    width:1200px;height:730px;overflow:hidden;
    background:var(--backdrop);
    font-family:"Montserrat",sans-serif;
  }
  .spread{
    position:absolute;left:40px;top:150px;
    width:1120px;height:430px;
    display:flex;
    box-shadow:0 12px 30px rgba(0,0,0,.25);
  }
  .page{position:relative;width:560px;height:430px;overflow:hidden;background:var(--paper);}
  .page--left{border-right:1px solid rgba(0,0,0,.08);}
  .bleed-photo{
    position:absolute;top:0;height:430px;
    background:linear-gradient(200deg,var(--photo-night) 0%,var(--photo-night) 22%,var(--photo-deep) 38%,var(--photo-blue) 60%,var(--photo-blue) 80%,var(--photo-deep) 100%);
  }
  .page--left .bleed-photo{left:390px;width:170px;
    background:linear-gradient(180deg,var(--photo-blue) 0%,var(--photo-blue) 70%,var(--photo-deep) 100%);}
  .page--right .bleed-photo{left:0;width:560px;}
  .lab-photo{
    position:absolute;left:14px;top:40px;width:376px;height:175px;
    background:linear-gradient(180deg,var(--lab-light) 0%,var(--lab-mid) 55%,#a9b6cc 100%);
  }
  .headline{
    position:absolute;left:60px;top:234px;width:320px;margin:0;
    font-weight:900;font-size:16px;line-height:20px;color:var(--navy);
    white-space:nowrap;
  }
  .body-col{
    position:absolute;top:266px;margin:0;
    font-size:8.5px;line-height:12.5px;color:var(--ink);
  }
  .body-col--one{left:60px;width:158px;}
  .body-col--two{left:230px;width:148px;}
  .folio{position:absolute;bottom:20px;font-size:7.5px;color:var(--muted);margin:0;}
  .folio--left{left:60px;}
  .folio--right{right:30px;color:rgba(255,255,255,.6);}
  .feature-panel{
    position:absolute;left:330px;top:60px;width:200px;
    padding:12px 14px 12px;box-sizing:border-box;
    background:rgba(27,33,48,.35);
  }
  .feature-title{margin:0 0 8px;font-weight:800;font-size:15px;line-height:17px;color:#fff;}
  .feature-body{margin:0;font-size:8px;line-height:12px;color:rgba(255,255,255,.9);}
</style>
</head>
<body>
  <div class="spread">
    <section class="page page--left">
      <div class="bleed-photo" role="img" aria-label="Mobile trailer laboratory unit parked outdoors, blue toned"></div>
      <div class="lab-photo" role="img" aria-label="Interior of a modular cleanroom laboratory with benches and chair"></div>
      <h2 class="headline">Headline Title or Product Number</h2>
      <p class="body-col body-col--one">Our modular cleanrooms arrive fully validated and ready for production. Each unit is built to exacting standards, tested in our own facility and shipped complete with utilities, controls and documentation so that your team can begin processing within weeks rather than months of construction.</p>
      <p class="body-col body-col--two">Flexible layouts support cell and gene therapy, vaccine filling and oncology research. Units can be joined, expanded or relocated as programs grow, keeping every stage of the product life cycle under one clean, controlled and fully monitored environment.</p>
      <p class="folio folio--left">6 | www.vitarun.com</p>
    </section>
    <section class="page page--right">
      <div class="bleed-photo" role="img" aria-label="Side of a white mobile trailer laboratory with doors and vents under trees at dusk, blue toned"></div>
      <div class="feature-panel">
        <h3 class="feature-title">Trailer<br>Laboratories</h3>
        <p class="feature-body">Our trailer laboratories bring containment to any site. Each mobile unit includes air handling, power, backup systems and biosafety cabinets. They deploy quickly for outbreak response, field testing or temporary capacity during expansion, and they can be parked beside existing buildings to extend research space without permanent construction work.</p>
      </div>
      <p class="folio folio--right">www.vitarun.com | 7</p>
    </section>
  </div>
</body>
</html>
```